User Photo Sharing Wordpress Design

We need a wordpress design that is ready launch-ready for our Company called Larkmesa. We allow users to submit their photos to our site in hopes that they will become the "Photo of the Day." Right now we are just running plug-ins to help with User submission but they do not accomplish our main goal: User submission goes directly to a created post and waits for admin approval of launch. We are specifically looking for a method integrated directly into wordpress that will allow users to submit their images and immediately, it automatically creates a post draft for the website admin to approve or deny. The user-submit area should collect the following data: Photo, Photo Information, First and Last name (or social media tag), Mobile Number, and Email List. We would suggest that the user can login to encourage loyalty and constant use.

This website also needs sufficient advertising space and a blog. We are looking to create something that is easy to replicate in multiple cities.

The final design should be ready to launch and be able to accomplish the main goal (successful photo sharing) at the minimum with a sleek design that is easy to use and is responsive.
Updates

Just as clarification... I am looking for a completed project that I can use on Wordpress ASAP.  This project has to allow my website visitors to upload their images and those images should be automatically loaded into a post and saved as a draft (or some variation of that process), allowing the website admin to approve or deny.  Information collecting is VITAL during the photo submission process.  This site needs to be responsive as well.  

Target Market(s)

Mostly Woman 13-65

Industry/Entity Type

Advertising

Requirements
Must have
• Photo submission methods allowing user to submit photos and admin to approve the created post.

Information collection (Name, Email, Mobile, Photo, Photo Info)
Nice to have
• Blog, photo segmentation, advertising room

```html
<!DOCTYPE html>
<html lang="en">
<head>
<meta charset="utf-8">
<title>Larkmesa – Photo of the Day</title>
<link rel="stylesheet" href="https://fonts.googleapis.com/css2?family=Oswald:wght@400;500;700&family=Open+Sans:ital,wght@0,400;0,600;1,400&display=swap">
<style>
:root{
  --page:#f3f3f2;
  --topbar:#3b3e43;
  --header:#e3eeee;
  --nav-active:#5b5e62;
  --ink:#3a3a3a;
  --muted:#777;
  --rule:#d8d8d6;
  --card:#ffffff;
  --accent:#c0392b;
  --footer:#1b1b1c;
  --footer-text:#bdbdbd;
}
*{box-sizing:border-box;margin:0;padding:0}
html,body{width:683px;height:1200px;overflow:hidden;background:var(--page);font-family:"Open Sans",Arial,sans-serif;color:var(--ink)}
.canvas{position:relative;width:683px;height:1200px;overflow:hidden}
.abs{position:absolute}
.heading{font-family:"Oswald",Arial Narrow,sans-serif;font-weight:400;text-transform:uppercase}

/* top bar */
.topbar{left:0;top:0;width:683px;height:18px;background:var(--topbar)}
.search-label{left:366px;top:5px;font-size:4.5px;color:#aaa;letter-spacing:.3px}
.search-box{left:388px;top:4px;width:94px;height:10px;background:#6c7075;border-radius:1px}
.search-icon{left:472px;top:5px}
.social{top:5px;width:8px;height:8px;border-radius:50%;background:#888c91}

/* header */
.header{left:0;top:18px;width:683px;height:47px;background:var(--header)}
.brand{left:103px;top:24px;font-family:"Oswald",sans-serif;font-weight:700;font-size:22px;line-height:1;color:#1a1a1a;letter-spacing:-.3px}
.brand-mark{left:196px;top:31px;width:9px;height:9px;border-radius:50%;background:#1a1a1a}
.nav-active{left:373px;top:18px;width:50px;height:47px;background:var(--nav-active)}
.nav-link{top:38px;font-family:"Oswald",sans-serif;font-size:7.5px;color:#5a5a5a;text-transform:uppercase}

/* hero */
.hero{left:0;top:65px;width:683px;height:250px;background:linear-gradient(100deg,#cfc3ae 0%,#b7a78c 30%,#8c8f9c 55%,#c9b797 80%,#d9cbb0 100%)}
.hero-caption{left:102px;top:153px;width:221px;height:69px;background:rgba(85,85,85,.78);padding:12px 0 0 16px}
.hero-caption p{font-family:"Oswald",sans-serif;font-size:19px;line-height:23px;color:#fff;text-transform:uppercase}
.hero-arrow{top:170px;width:36px;height:36px;border-radius:50%;background:rgba(120,120,120,.55)}

/* photo of the day */
.section-title{left:0;width:683px;text-align:center;top:327px;font-size:17px;color:#333}
.section-sub{left:0;width:683px;text-align:center;top:353px;font-family:"Oswald",sans-serif;font-size:7.5px;color:#333;text-transform:uppercase}
.rule{left:102px;width:479px;height:2px;border-top:1px solid var(--rule);border-bottom:1px solid #fff}
.card{width:111px;height:178px;background:var(--card);border:1px solid #e2e2e0;box-shadow:0 1px 2px rgba(0,0,0,.06)}
.card-photo{position:absolute;left:5px;top:5px;width:100px;height:116px}
.card-title{position:absolute;left:0;width:100%;top:128px;text-align:center;font-family:"Oswald",sans-serif;font-size:6.5px;color:#666;text-transform:uppercase}
.card-credit{position:absolute;left:0;width:100%;top:139px;text-align:center;font-size:3.8px;color:#888;text-transform:uppercase}
.card-date{position:absolute;left:0;width:100%;top:148px;text-align:center;font-size:4px;font-style:italic;color:#888}
.card-meta{position:absolute;left:0;width:100%;top:164px;text-align:center;font-size:4px;font-style:italic;color:#888}
.card-meta b{display:inline-block;width:5px;height:4px;background:#444;margin:0 2px 0 6px;vertical-align:middle}

.pager{top:772px;height:14px;display:flex;gap:2px;right:105px}
.pager span{display:block;height:14px;padding:0 5px;border:1px solid #ddd;background:#fff;font-size:6px;line-height:12px;color:var(--accent)}
.pager span.current{background:#eee;color:#888}

.ad{left:159px;top:801px;width:356px;height:44px;background:linear-gradient(90deg,#b33a2a 0%,#c4472f 40%,#5d9a2f 70%,#4a8a27 100%);border:1px solid #888}

/* blog */
.blog-title{left:102px;top:879px;font-size:12.5px;color:#333}
.blog-intro{left:103px;top:901px;width:100px;font-size:4.6px;line-height:8.7px;color:#444}
.blog-divider{left:211px;top:883px;width:1px;height:70px;background:var(--rule)}
.arrow-btn{width:13px;height:13px;background:#c9c9c9;border:1px solid #bdbdbd}
.post{width:108px}
.post-photo{width:108px;height:64px}
.post-title{margin-top:8px;font-family:"Oswald",sans-serif;font-size:5.8px;line-height:9px;color:#444;text-transform:uppercase}
.post-text{margin-top:3px;font-size:4.5px;line-height:8.7px;color:#555}
.post-date{margin-top:2px;font-size:4px;font-style:italic;color:#888}

/* gallery */
.gallery-title{left:102px;top:1029px;font-size:12.5px;color:#333}
.thumb{top:1057px;width:88px;height:58px}
.thumb-shadow{top:1118px;width:88px;height:6px;background:radial-gradient(ellipse at center,rgba(0,0,0,.22) 0%,rgba(0,0,0,0) 70%)}

/* footer */
.footer{left:0;top:1140px;width:683px;height:60px;background:var(--footer)}
.footer-label{font-family:"Oswald",sans-serif;font-size:7.5px;color:#ddd;text-transform:uppercase}
.footer-input{left:102px;top:1170px;width:105px;height:14px;background:#2a2a2b;font-size:4.5px;color:#888;padding:4px 6px;text-transform:uppercase}
.footer-btn{left:210px;top:1170px;width:46px;height:14px;background:#2f2f30;font-size:4.5px;color:#999;text-align:center;line-height:14px;text-transform:uppercase}
.partner{left:340px;top:1156px;font-family:"Open Sans",sans-serif;font-weight:600;font-size:7px;color:#bbb}
.partner-mark{left:336px;top:1153px;width:62px;height:26px;border-radius:2px;background:#2c2c2d}
.footer-links{left:432px;top:1160px;font-size:4px;color:#8a8a8a;text-transform:uppercase;word-spacing:1px}
.footer-copy{left:432px;top:1170px;font-size:4px;color:#777;text-transform:uppercase}
</style>
</head>
<body>
<div class="canvas">

  <!-- top bar -->
  <div class="abs topbar"></div>
  <div class="abs search-label">SEARCH:</div>
  <div class="abs search-box"></div>
  <svg class="abs search-icon" width="8" height="8" viewBox="0 0 8 8"><circle cx="3.2" cy="3.2" r="2.2" fill="none" stroke="#ddd" stroke-width="1"/><line x1="4.8" y1="4.8" x2="7" y2="7" stroke="#ddd" stroke-width="1"/></svg>
  <div class="abs social" style="left:495px"></div>
  <div class="abs social" style="left:514px"></div>
  <div class="abs social" style="left:534px"></div>
  <div class="abs social" style="left:553px"></div>
  <div class="abs social" style="left:572px"></div>

  <!-- header -->
  <header class="abs header"></header>
  <div class="abs brand">Larkmesa</div>
  <div class="abs nav-active"></div>
  <div class="abs nav-link" style="left:389px;color:#eee">Home</div>
  <div class="abs nav-link" style="left:447px">Photo of the Day</div>
  <div class="abs nav-link" style="left:543px">About</div>

  <!-- hero -->
  <div class="abs hero" role="img" aria-label="Hero photograph of a bicycle leaning in warm sunlight on a street"></div>
  <div class="abs hero-arrow" style="left:56px"></div>
  <svg class="abs" style="left:69px;top:180px" width="10" height="16" viewBox="0 0 10 16"><polyline points="8,1 2,8 8,15" fill="none" stroke="#eee" stroke-width="1.2"/></svg>
  <div class="abs hero-arrow" style="left:587px"></div>
  <svg class="abs" style="left:600px;top:180px" width="10" height="16" viewBox="0 0 10 16"><polyline points="2,1 8,8 2,15" fill="none" stroke="#eee" stroke-width="1.2"/></svg>
  <div class="abs hero-caption"><p>Shoot it! &amp; Share it!</p><p>Larkmesa.com</p></div>

  <!-- photo of the day -->
  <h1 class="abs heading section-title">Photo of the Day</h1>
  <p class="abs section-sub">Larkmesa's only photo sharing website, featuring your photos for free. Submit your photos now!</p>
  <div class="abs rule" style="top:375px"></div>

  <div class="abs card" style="left:104px;top:390px"><div class="card-photo" role="img" aria-label="Dark stormy sky over a building" style="background:linear-gradient(180deg,#4a4d52,#1d1e21)"></div><div class="card-title">Biking on the Parkway</div><div class="card-credit">Another great shot by @Ridgeline247!</div><div class="card-date">May 23, 2013 -Picture of the Day</div><div class="card-meta"><b></b>0 Comments <b></b>Reactions</div></div>
  <div class="abs card" style="left:225px;top:390px"><div class="card-photo" role="img" aria-label="Campus building with lawn and blue sky" style="background:linear-gradient(180deg,#3aa0d8 0%,#b06040 45%,#4f8a3a 100%)"></div><div class="card-title">Biking on the Parkway</div><div class="card-credit">Another great shot by @Ridgeline247!</div><div class="card-date">May 23, 2013 -Picture of the Day</div><div class="card-meta"><b></b>0 Comments <b></b>Reactions</div></div>
  <div class="abs card" style="left:346px;top:390px"><div class="card-photo" role="img" aria-label="Winding road through winter hills" style="background:linear-gradient(180deg,#5b6f8a 0%,#8d7d6e 40%,#6b5a4c 100%)"></div><div class="card-title">Biking on the Parkway</div><div class="card-credit">Another great shot by @Ridgeline247!</div><div class="card-date">May 23, 2013 -Picture of the Day</div><div class="card-meta"><b></b>0 Comments <b></b>Reactions</div></div>
  <div class="abs card" style="left:468px;top:390px"><div class="card-photo" role="img" aria-label="Town main street with passing cars" style="background:linear-gradient(180deg,#e7d85a 0%,#9a5a3c 40%,#6d6a66 100%)"></div><div class="card-title">Biking on the Parkway</div><div class="card-credit">Another great shot by @Ridgeline247!</div><div class="card-date">May 23, 2013 -Picture of the Day</div><div class="card-meta"><b></b>0 Comments <b></b>Reactions</div></div>

  <div class="abs card" style="left:104px;top:581px"><div class="card-photo" role="img" aria-label="Red sunset over snowy town" style="background:linear-gradient(180deg,#e0505a 0%,#b83a3a 40%,#3d2a30 100%)"></div><div class="card-title">Biking on the Parkway</div><div class="card-credit">Another great shot by @Ridgeline247!</div><div class="card-date">May 23, 2013 -Picture of the Day</div><div class="card-meta"><b></b>0 Comments <b></b>Reactions</div></div>
  <div class="abs card" style="left:225px;top:581px"><div class="card-photo" role="img" aria-label="Purple toned lettered bridge photo" style="background:linear-gradient(180deg,#8a7aa8,#5a4a6e)"></div><div class="card-title">Biking on the Parkway</div><div class="card-credit">Another great shot by @Ridgeline247!</div><div class="card-date">May 23, 2013 -Picture of the Day</div><div class="card-meta"><b></b>0 Comments <b></b>Reactions</div></div>
  <div class="abs card" style="left:346px;top:581px"><div class="card-photo" role="img" aria-label="Snow covered parking lot by apartments" style="background:linear-gradient(180deg,#d8d8d8,#7a7a7a)"></div><div class="card-title">Biking on the Parkway</div><div class="card-credit">Another great shot by @Ridgeline247!</div><div class="card-date">May 23, 2013 -Picture of the Day</div><div class="card-meta"><b></b>0 Comments <b></b>Reactions</div></div>
  <div class="abs card" style="left:468px;top:581px"><div class="card-photo" role="img" aria-label="Mountain valley view under cloudy sky" style="background:linear-gradient(180deg,#5a6f95 0%,#9a8d88 45%,#6a4a30 100%)"></div><div class="card-title">Biking on the Parkway</div><div class="card-credit">Another great shot by @Ridgeline247!</div><div class="card-date">May 23, 2013 -Picture of the Day</div><div class="card-meta"><b></b>0 Comments <b></b>Reactions</div></div>

  <nav class="abs pager"><span class="current">1</span><span>2</span><span>3</span><span>4</span><span>5</span><span>10</span><span>20</span><span>30</span><span>Next »</span><span>Last »</span></nav>

  <div class="abs ad" role="img" aria-label="Advertising banner for Trackwinner racing tips, latest winner Stormrunner"></div>

  <div class="abs rule" style="top:862px"></div>

  <!-- blog -->
  <h2 class="abs heading blog-title">From the Blog</h2>
  <p class="abs blog-intro">when an unknown printer took a galley of type and scrambled it to make a type specimen book. It has survived not only five centuries, but also the leap into electronic typesetting, remaining essentially unchanged.</p>
  <div class="abs blog-divider"></div>
  <div class="abs arrow-btn" style="left:103px;top:971px"></div>
  <div class="abs arrow-btn" style="left:119px;top:971px"></div>
  <svg class="abs" style="left:107px;top:974px" width="28" height="7" viewBox="0 0 28 7"><polyline points="4,0.5 1.5,3.5 4,6.5" fill="none" stroke="#fff" stroke-width="1"/><polyline points="19,0.5 21.5,3.5 19,6.5" fill="none" stroke="#fff" stroke-width="1"/></svg>

  <article class="abs post" style="left:232px;top:883px"><div class="post-photo" role="img" aria-label="Family silhouetted against a lake at dusk" style="background:linear-gradient(180deg,#5c6a7c,#2a3240)"></div><h3 class="post-title">Pinecrest Summit // Perfect Photo Shoot</h3><p class="post-text">Are you looking for the best location in North Carolina to have a landscape photo shoot?...</p><p class="post-date">Posted on May 23, 2013</p></article>
  <article class="abs post" style="left:353px;top:883px"><div class="post-photo" role="img" aria-label="Couple portrait in warm autumn light" style="background:linear-gradient(135deg,#c89a70,#6a4a38)"></div><h3 class="post-title">Mara Lindqvist Photography</h3><p class="post-text">Are you looking for the best location in North Carolina to have a landscape photo shoot?...</p><p class="post-date">Posted on May 23, 2013</p></article>
  <article class="abs post" style="left:473px;top:883px"><div class="post-photo" role="img" aria-label="Green trees by a misty field" style="background:linear-gradient(180deg,#b8c2b6,#6f7f56)"></div><h3 class="post-title">Ridgeline247</h3><p class="post-text">Are you looking for the best location in North Carolina to have a landscape photo shoot?...</p><p class="post-date">Posted on May 23, 2013</p></article>

  <div class="abs rule" style="top:1022px"></div>

  <!-- gallery -->
  <h2 class="abs heading gallery-title">Photo Gallery</h2>
  <div class="abs arrow-btn" style="left:553px;top:1036px"></div>
  <div class="abs arrow-btn" style="left:569px;top:1036px"></div>
  <svg class="abs" style="left:557px;top:1039px" width="28" height="7" viewBox="0 0 28 7"><polyline points="4,0.5 1.5,3.5 4,6.5" fill="none" stroke="#fff" stroke-width="1"/><polyline points="19,0.5 21.5,3.5 19,6.5" fill="none" stroke="#fff" stroke-width="1"/></svg>

  <div class="abs thumb" style="left:102px;background:linear-gradient(180deg,#d8b888,#6a5030)" role="img" aria-label="City skyline at golden hour over a harbor"></div>
  <div class="abs thumb" style="left:199px;background:linear-gradient(180deg,#2a2a2a,#8a8a8a)" role="img" aria-label="Black and white night street"></div>
  <div class="abs thumb" style="left:297px;background:linear-gradient(180deg,#5a3a2a,#c07040)" role="img" aria-label="Lit shopping street at night"></div>
  <div class="abs thumb" style="left:395px;background:linear-gradient(180deg,#1e1e1e,#7a7a7a)" role="img" aria-label="Monochrome city intersection at night"></div>
  <div class="abs thumb" style="left:493px;background:linear-gradient(180deg,#6a6a6a,#a89a86)" role="img" aria-label="Downtown avenue between tall buildings"></div>
  <div class="abs thumb-shadow" style="left:102px"></div>
  <div class="abs thumb-shadow" style="left:199px"></div>
  <div class="abs thumb-shadow" style="left:297px"></div>
  <div class="abs thumb-shadow" style="left:395px"></div>
  <div class="abs thumb-shadow" style="left:493px"></div>

  <!-- footer -->
  <footer class="abs footer"></footer>
  <div class="abs footer-label" style="left:103px;top:1153px">Mailing List Signup</div>
  <div class="abs footer-input">Enter your email ID :</div>
  <div class="abs footer-btn">Subscribe</div>
  <div class="abs footer-label" style="left:273px;top:1173px">Media Friends</div>
  <div class="abs partner-mark"></div>
  <div class="abs partner" style="left:341px;top:1171px">Ridgeline247</div>
  <div class="abs footer-links">Photo of the Day &nbsp; | &nbsp; Blog &nbsp; | &nbsp; Photo Gallery</div>
  <div class="abs footer-copy">© Copyright - Larkmesa : Privacy Policy &nbsp;Terms &amp; Conditions</div>
</div>
</body>
</html>
```